Chic streamline modern edgy! Danemerecurls.com

I need a website built for my personal business. I am a hair stylist and I would like a crisp website that works well, is sleek, easy to use, and allows my clients to navigate through Services and pay deposits for services listed.

My logo is somewhat of a full moon, so my theme is nocturnal.

My information can be found at chairbook.com/danemerecurls

Target Market(s)

Women ages 25-55 who are looking for luxury hair extension services

Industry/Entity Type

Hair And Beauty

Number of Pages Required

1 page

Colors
474747
919191
d3d3d3
000000

Requirements
Must have
• Location map, coinvale link embedded for deposits, contact box, bio, faq/policies, menu of services, hours of availability by appointment only .
Nice to have
• An interactive calander where I could post dates that I am available, preferred providers for other beauty services where i could list other websites for make up and other beauty related referrals. a bridal tab would be nice to offer information about bridal services and policies.

```html
<!DOCTYPE html>
<html lang="en">
<head>
<meta charset="utf-8">
<title>Danemere Curls</title>
<link rel="stylesheet" href="https://fonts.googleapis.com/css2?family=Raleway:wght@300;400;500;600&family=Lato:wght@400;700&display=swap">
<style>
:root{
  --ink:#000000;
  --charcoal:#1a1a1a;
  --slate:#474747;
  --mid:#919191;
  --silver:#d3d3d3;
  --white:#ffffff;
  --field:#5a5a5a;
  --card:#4a4a4a;
  --card-frame:#6a6a6a;
}
*{box-sizing:border-box;margin:0;padding:0}
html,body{width:1200px;height:3468px;overflow:hidden}
body{position:relative;background:var(--ink);font-family:'Lato',sans-serif;color:var(--white)}
.abs{position:absolute}
.fill{position:absolute}
.heading{font-family:'Raleway',sans-serif;font-weight:400;color:var(--white);letter-spacing:1px}
.heading .soft{color:var(--mid);font-weight:300}
.btn{position:absolute;display:flex;align-items:center;justify-content:center;font-family:'Lato',sans-serif;font-weight:700;font-size:13px;letter-spacing:.5px;color:#2a2a2a;background:linear-gradient(#f0f0f0,#c9c9c9);border:1px solid #888;border-radius:3px}

/* top bar */
.topbar{position:absolute;left:0;top:0;width:1200px;height:37px;background:#2b2b2b}
.pay-badge{position:absolute;left:52px;top:5px;width:140px;height:26px;border-radius:13px;background:var(--silver);display:flex;align-items:center;justify-content:center;gap:8px;font-family:'Raleway',sans-serif;font-weight:600;font-size:14px;color:#333}
.pay-badge i{width:10px;height:10px;border-radius:50%;background:#333;display:block}
.top-contact{position:absolute;top:0;height:37px;display:flex;align-items:center;gap:8px;font-size:14px;color:var(--silver)}
.top-contact .dot{width:22px;height:22px;border-radius:50%;background:var(--white);display:flex;align-items:center;justify-content:center}

/* header */
.header{position:absolute;left:0;top:37px;width:1200px;height:74px;background:var(--white);border-bottom:1px solid #ddd}
.logo{position:absolute;display:flex;align-items:center;gap:14px;font-family:'Raleway',sans-serif;font-weight:400;letter-spacing:1px}
.logo .moon{border-radius:50%;background:#333}
.nav{position:absolute;right:72px;top:14px;display:flex;gap:6px}
.nav a{display:block;padding:12px 18px;font-family:'Raleway',sans-serif;font-weight:500;font-size:15px;color:#333;text-decoration:none}
.nav a.active{border:2px solid #333;padding:10px 16px}

/* hero */
.hero{position:absolute;left:0;top:111px;width:1200px;height:543px;background:linear-gradient(90deg,#cfc7c0 0%,#d8d4d1 35%,#cfcfcf 60%,#bdbdbd 100%)}
.hero-title{position:absolute;right:96px;top:105px;text-align:right;font-family:'Raleway',sans-serif;font-weight:400;font-size:50px;line-height:68px;color:#1e1e1e}
.hero-sub{position:absolute;right:96px;top:255px;text-align:right;font-family:'Raleway',sans-serif;font-weight:400;font-size:26px;line-height:40px;color:#555}
.hero-btn{position:absolute;left:862px;top:362px;width:234px;height:48px;border:2px solid #222;display:flex;align-items:center;justify-content:center;font-family:'Raleway',sans-serif;font-weight:600;font-size:15px;color:#222}

/* about */
.about{position:absolute;left:0;top:654px;width:1200px;height:444px;background:var(--charcoal)}
.about-text{position:absolute;left:55px;top:128px;width:640px;font-size:13.5px;line-height:25px;color:var(--mid)}

/* services */
.services{position:absolute;left:0;top:1098px;width:1200px;height:571px;background:#080808}
.section-sub{position:absolute;left:0;width:1200px;text-align:center;font-size:14px;color:var(--silver)}
.card{position:absolute;top:171px;width:257px;height:342px;background:var(--card);border:5px solid var(--card-frame)}
.card .photo{position:absolute;left:0;top:0;width:247px;height:182px}
.card h3{position:absolute;left:0;top:206px;width:247px;text-align:center;font-family:'Raleway',sans-serif;font-weight:600;font-size:23px;color:var(--white)}
.card p{position:absolute;left:20px;top:248px;width:207px;text-align:center;font-size:13.5px;line-height:25px;color:#8a8a8a}
.card .go{position:absolute;left:106px;top:304px;width:36px;height:34px;background:#8a8a8a;border-radius:2px;display:flex;align-items:center;justify-content:center}

/* gallery */
.gallery{position:absolute;left:0;top:1669px;width:1200px;height:759px;background:#151515}
.tile{position:absolute}

/* booking */
.booking{position:absolute;left:0;top:2428px;width:1200px;height:439px;background:linear-gradient(90deg,#4a4a4a,#3c3c3c)}
.booking .portrait{position:absolute;left:0;top:0;width:455px;height:439px;background:linear-gradient(160deg,#f4f4f4 30%,#9a9a9a 70%,#5a5a5a)}
.field{position:absolute;height:44px;background:var(--field);border:1px solid #666;display:flex;align-items:center;justify-content:space-between;padding:0 14px;font-size:13px;color:#8c8c8c}

/* contact */
.contact{position:absolute;left:0;top:2867px;width:1200px;height:485px;background:#121212}
.divider{position:absolute;top:140px;width:1px;height:240px;background:#333}
.info{position:absolute;left:540px;font-size:14px;line-height:24px;color:var(--silver)}
.info b{color:var(--white);font-weight:700}
.info-icon{position:absolute;left:494px;width:28px;height:28px;border-radius:50%;background:#333;display:flex;align-items:center;justify-content:center}
.social{position:absolute;left:1005px;display:flex;align-items:center;gap:16px;font-size:14px;color:var(--silver)}
.social i{display:block;width:36px;height:36px;border-radius:50%}

/* footer */
.footer{position:absolute;left:0;top:3352px;width:1200px;height:116px;background:#2a2a2a;border-top:1px solid #3a3a3a}
.footer-links{position:absolute;left:55px;top:28px;display:flex;font-size:14px;color:var(--silver)}
.footer-links span{padding:0 18px;border-left:1px solid #555}
.footer-links span:first-child{padding-left:0;border-left:0}
.copyright{position:absolute;left:55px;top:64px;font-size:12px;color:#8a8a8a}
</style>
</head>
<body>

<div class="topbar">
  <div class="pay-badge"><i></i>Coinvale</div>
  <div class="top-contact" style="left:810px">
    <span class="dot"><svg width="12" height="9" viewBox="0 0 12 9"><rect x=".5" y=".5" width="11" height="8" fill="none" stroke="#333"/><path d="M.5 .5 6 5l5.5-4.5" fill="none" stroke="#333"/></svg></span>
    info@danemerecurls.com
  </div>
  <div class="top-contact" style="left:1022px">
    <span class="dot"><svg width="12" height="12" viewBox="0 0 12 12"><path d="M2 1l2 0 1 3-1.5 1a7 7 0 0 0 3.5 3.5L8 7l3 1v2a1 1 0 0 1-1 1A9 9 0 0 1 1 2a1 1 0 0 1 1-1z" fill="#333"/></svg></span>
    555-014-2290
  </div>
</div>

<header class="header">
  <div class="logo" style="left:55px;top:17px;font-size:30px;color:#222">DANEMERE CURLS <span class="moon" style="width:38px;height:38px"></span></div>
  <nav class="nav">
    <a class="active">Home</a><a>About Me</a><a>Services</a><a>Photo Gallery</a><a>Contact Us</a>
  </nav>
  <svg class="abs" style="left:1122px;top:26px" width="22" height="22" viewBox="0 0 22 22"><circle cx="9" cy="9" r="6.5" fill="none" stroke="#333" stroke-width="2.5"/><path d="M14 14l6 6" stroke="#333" stroke-width="3"/></svg>
</header>

<section class="hero">
  <div class="fill" role="img" aria-label="Portrait of a woman with long auburn curls" style="left:0;top:0;width:620px;height:543px;background:linear-gradient(135deg,#c9b8a8,#8a5a3c 55%,#cfc3b6)"></div>
  <div class="hero-title">Creative, Classic<br>Distinguished</div>
  <div class="hero-sub">Get The Most Beautiful<br>Hairs Inside &amp; Out!</div>
  <div class="hero-btn">BOOK AN APPOINTMENT</div>
</section>

<section class="about">
  <h2 class="heading abs" style="left:55px;top:52px;font-size:44px">ABOUT <span class="soft">DANEMERE CURLS</span></h2>
  <p class="about-text">Welcome to a studio built around you. Every appointment begins with a calm consultation where we talk through your hair history, your routine and the look you want to wear. From soft everyday waves to full luxury extensions, each service is shaped by hand with premium products and patient care. The studio is open Tuesday to Saturday, 9am to 7pm, by appointment only, so your chair is never rushed. A deposit secures every booking and is applied to your service total. Please give 48 hours notice to reschedule; late cancellations and missed visits forfeit the deposit. Arrive with clean, dry hair unless told otherwise, and allow extra time for extension installs. Bridal parties are welcome with a consultation booked in advance.</p>
  <div class="btn" style="left:60px;top:352px;width:130px;height:38px">View Gallery</div>
  <div class="fill" role="img" aria-label="Stylist cutting hair with comb and scissors" style="left:745px;top:0;width:455px;height:444px;background:linear-gradient(135deg,#3a2a1c,#8a5a30 50%,#2a1a10)"></div>
</section>

<section class="services">
  <h2 class="heading abs" style="left:0;top:42px;width:1200px;text-align:center;font-size:46px">OUR SERVICES</h2>
  <p class="section-sub" style="top:107px">Luxury hair care and extensions tailored to the woman you are</p>

  <div class="card" style="left:53px">
    <div class="photo" role="img" aria-label="Stylist styling a client's hair in a salon" style="background:linear-gradient(135deg,#d8d0c6,#8a6a50)"></div>
    <h3>Basic Hair Styling</h3>
    <p>Soft shape and finish for daily wear</p>
    <span class="go"><svg width="10" height="14" viewBox="0 0 10 14"><path d="M2 1l6 6-6 6" fill="none" stroke="#fff" stroke-width="2.5"/></svg></span>
  </div>
  <div class="card" style="left:333px">
    <div class="photo" role="img" aria-label="Hair colour being brushed onto a foil section" style="background:linear-gradient(135deg,#e0d6cc,#7a4a2a)"></div>
    <h3>Hair Coloring</h3>
    <p>Rich custom tones blended by hand</p>
    <span class="go"><svg width="10" height="14" viewBox="0 0 10 14"><path d="M2 1l6 6-6 6" fill="none" stroke="#fff" stroke-width="2.5"/></svg></span>
  </div>
  <div class="card" style="left:613px">
    <div class="photo" role="img" aria-label="Extension strands being bonded with a heat tool" style="background:linear-gradient(135deg,#6a4028,#c8a080 60%,#d8d0c8)"></div>
    <h3>Hair Extensions</h3>
    <p>Seamless length and volume that lasts</p>
    <span class="go"><svg width="10" height="14" viewBox="0 0 10 14"><path d="M2 1l6 6-6 6" fill="none" stroke="#fff" stroke-width="2.5"/></svg></span>
  </div>
  <div class="card" style="left:893px">
    <div class="photo" role="img" aria-label="Flat iron straightening long brown hair" style="background:linear-gradient(135deg,#d0c8c0,#5a3a26)"></div>
    <h3>Straightening</h3>
    <p>Smooth sleek results with lasting shine</p>
    <span class="go"><svg width="10" height="14" viewBox="0 0 10 14"><path d="M2 1l6 6-6 6" fill="none" stroke="#fff" stroke-width="2.5"/></svg></span>
  </div>
</section>

<section class="gallery">
  <h2 class="heading abs" style="left:0;top:44px;width:1200px;text-align:center;font-size:46px">Photo <span class="soft">Gallery</span></h2>
  <p class="section-sub" style="top:108px;color:var(--mid)">A look at recent styles, colour work and extensions from the studio chair</p>
  <div class="tile" role="img" aria-label="Woman with voluminous bouncy curls" style="left:55px;top:174px;width:433px;height:434px;background:linear-gradient(135deg,#6a4a38,#c0a088 50%,#3a2a20)"></div>
  <div class="tile" role="img" aria-label="Close-up of scissors trimming hair" style="left:492px;top:174px;width:433px;height:212px;background:linear-gradient(135deg,#e8e2dc,#4a3a30)"></div>
  <div class="tile" role="img" aria-label="Woman with long wavy hair" style="left:929px;top:174px;width:216px;height:212px;background:linear-gradient(135deg,#3a2418,#a06a48)"></div>
  <div class="tile" role="img" aria-label="Woman with sleek straight copper hair" style="left:492px;top:391px;width:215px;height:217px;background:linear-gradient(135deg,#8a4a28,#d8a070)"></div>
  <div class="tile" role="img" aria-label="Hair wrapped around purple rollers" style="left:714px;top:391px;width:431px;height:217px;background:linear-gradient(135deg,#d8d0d0,#6a4a70 50%,#4a3020)"></div>
  <div class="btn" style="left:483px;top:657px;width:238px;height:39px;font-size:12px">VIEW ALL PHOTO GALLERIES</div>
</section>

<section class="booking">
  <div class="portrait" role="img" aria-label="Black and white portrait of a man in a patterned jacket"></div>
  <h2 class="heading abs" style="left:509px;top:44px;font-size:46px">Book An <span class="soft">Appointment</span></h2>
  <div class="field" style="left:513px;top:136px;width:301px">Name</div>
  <div class="field" style="left:844px;top:136px;width:296px">Email Id</div>
  <div class="field" style="left:513px;top:196px;width:301px">Service/Treatment <svg width="10" height="6" viewBox="0 0 10 6"><path d="M0 0h10L5 6z" fill="#8c8c8c"/></svg></div>
  <div class="field" style="left:837px;top:196px;width:139px">Date <svg width="14" height="14" viewBox="0 0 14 14"><rect x="1" y="2" width="12" height="11" fill="none" stroke="#8c8c8c" stroke-width="1.5"/><path d="M1 5h12" stroke="#8c8c8c" stroke-width="1.5"/></svg></div>
  <div class="field" style="left:999px;top:196px;width:141px">Time <svg width="10" height="6" viewBox="0 0 10 6"><path d="M0 0h10L5 6z" fill="#8c8c8c"/></svg></div>
  <div class="field" style="left:513px;top:256px;width:627px;height:65px;align-items:flex-start;padding-top:10px">Comments</div>
  <div class="btn" style="left:513px;top:342px;width:176px;height:46px;font-size:13px">GET APPOINTMENT</div>
</section>

<section class="contact">
  <h2 class="heading abs" style="left:0;top:40px;width:1200px;text-align:center;font-size:46px">Contact <span class="soft">Details</span></h2>
  <div class="fill" role="img" aria-label="Street map showing the studio location" style="left:78px;top:122px;width:292px;height:292px;border-radius:50%;border:6px solid #fff;background:radial-gradient(circle,#f2ecd8,#d8e4c8 60%,#b8cce0)"></div>
  <div class="divider" style="left:430px"></div>
  <div class="divider" style="left:890px"></div>

  <span class="info-icon" style="top:145px"><svg width="10" height="14" viewBox="0 0 10 14"><path d="M5 0a5 5 0 0 1 5 5c0 4-5 9-5 9S0 9 0 5a5 5 0 0 1 5-5z" fill="#fff"/><circle cx="5" cy="5" r="2" fill="#333"/></svg></span>
  <div class="info" style="top:146px;width:320px"><b>DANEMERE CURLS</b><br>14 Nightfall Lane, Suite 2 · Open Tue–Sat 9am–7pm, by appointment only</div>

  <span class="info-icon" style="top:254px"><svg width="12" height="12" viewBox="0 0 12 12"><path d="M2 1l2 0 1 3-1.5 1a7 7 0 0 0 3.5 3.5L8 7l3 1v2a1 1 0 0 1-1 1A9 9 0 0 1 1 2a1 1 0 0 1 1-1z" fill="#fff"/></svg></span>
  <div class="info" style="top:256px">Call Us At,<br><b style="font-size:15px">(555) - 014 - 2290</b></div>

  <span class="info-icon" style="top:330px"><svg width="12" height="9" viewBox="0 0 12 9"><rect x=".5" y=".5" width="11" height="8" fill="#fff"/><path d="M.5 .5 6 5l5.5-4.5" fill="none" stroke="#333"/></svg></span>
  <div class="info" style="top:332px">Write To Us,<br><b>info@danemerecurls.com</b></div>

  <div class="social" style="top:141px"><i style="background:#3b5998"></i>Facenote</div>
  <div class="social" style="top:204px"><i style="background:#0077b5"></i>Linkwork</div>
  <div class="social" style="top:266px"><i style="background:#1da1f2"></i>Chirper</div>
  <div class="social" style="top:331px"><i style="background:#dd4b39"></i>Searchplus</div>
</section>

<footer class="footer">
  <div class="footer-links"><span>Home</span><span>About Me</span><span>Services</span><span>Photo Gallery</span><span>Contact Us</span></div>
  <div class="copyright">Copyright 2016 DANEMERE CURLS | All Rights Reserved.</div>
  <div class="logo" style="left:745px;top:32px;font-size:36px;color:#fff">DANEMERE CURLS <span class="moon" style="width:50px;height:50px;background:#d3d3d3"></span></div>
</footer>

</body>
</html>
```